Brandor Letterhead/Business Card Redesign

PLEASE USE THE LOGO'S IN THE ZIP FILE (BRANDOR LOGO MAIN LOGO - QM-7 AND VESPANE SUB LOGOS - MAYBE 30% OF BRANDOR SIZE). THE OTHER FILES DONT OPEN FOR SOME REASON! THANKS!!

We need a new letterhead and business card for our UK Engineering supplies organisation.

We are looking for an image that convey high quality and performance, being proffesional and bold.

Our company sells engineering tooling accessories to business customers throughout the UK. We are agents for two companies, QM-7 and Vespane Inc, their logo's should be incorporated as a sub part of the design with the emphasis on the Brandor logo.

Designs must be editable on PC versions of illustrator.

Company Details for letterhead
Brandor Limited
Hollin Offices
Hollin Street
Ashbrook
West Ardenshire
United Kingdom
Tel: 01632 470215
Fax: 01632 470216
Email: sales@brandor.net
www.brandorparts.co.uk

Company Registration 5817403
Vat No 418 2075 36

Name for business card
Pete Moxham
General Manager
pete@brandor.net
Updates

This project is now guaranteed payment and I have increased the budget 

Target Market(s)

Business to Business buyers in the engineering industry

Industry/Entity Type

Business

Requirements
Must have
• Brandor logo as main logog with sub-logos from Vespane and QM-7.
• Include the message on the letterhead "Next Day Delivery of Cutting Tools & Machine Tool Accessories in the UK & Ireland".
Nice to have
• I will supply some pictures of our products, if they can be incorporated into the design then it could be good.

```html
<!DOCTYPE html>
<html lang="en">
<head>
<meta charset="utf-8">
<title>Brandor Stationery</title>
<link rel="stylesheet" href="https://fonts.googleapis.com/css2?family=Source+Sans+3:wght@300;400;600;700&display=swap">
<style>
:root{
  --stage:#000;
  --paper:#fff;
  --ink:#3a3a3a;
  --cyan:#00e8f0;
  --cyan-deep:#00b8e6;
  --guide:#d6f3f6;
  --tile:#f1fbfd;
  --grid:#cdeef5;
  --steel:#b9bdbf;
}
*{margin:0;padding:0;box-sizing:border-box}
html,body{width:1200px;height:900px;overflow:hidden;background:var(--stage)}
body{position:relative;font-family:"Source Sans 3",Arial,sans-serif;font-weight:300;color:var(--ink)}
.abs{position:absolute}

/* letterhead */
.letterhead{left:153px;top:33px;width:590px;height:835px;background:var(--paper)}
.guide-v{position:absolute;top:0;bottom:0;width:1px;background:var(--guide)}
.guide-h{position:absolute;left:0;width:50px;height:1px;background:var(--guide)}
.guide-hr{position:absolute;left:466px;width:102px;height:1px;background:var(--guide)}
.letter{position:absolute;left:56px;font-size:10.6px;line-height:13px}
.letter p{margin-bottom:13px}
.date{top:26px}
.recipient{top:144px}
.body{top:299px;width:376px}
.signoff{top:543px}
.signname{top:608px}

.brand-mark{display:flex;align-items:center;gap:5px;font-weight:700;color:var(--cyan-deep);letter-spacing:1px;white-space:nowrap}
.brand-mark .dot{border-radius:50%;background:var(--cyan-deep);flex:none}
.lh-logo{left:462px;top:72px;font-size:16px}
.lh-logo .dot{width:13px;height:13px}

.address{left:470px;top:144px;font-size:8.6px;line-height:10px}
.address .gap{height:5px}
.address b{color:var(--cyan-deep);font-weight:700}
.address .web{font-weight:600;color:#222;margin-top:5px;font-size:8.8px}

.tagline{color:var(--cyan);font-size:8.4px;line-height:10px;font-weight:400}
.tagline strong{font-weight:700}
.lh-tagline{left:470px;top:299px}

.product-grid{left:466px;top:484px;width:102px;height:253px;border:1px solid var(--guide);
  background-color:var(--tile);
  background-image:linear-gradient(var(--grid) 1px,transparent 1px),linear-gradient(90deg,var(--grid) 1px,transparent 1px);
  background-size:8px 8px}
.product{position:absolute;background:linear-gradient(160deg,#e3e5e6,var(--steel) 60%,#8d9294)}
.p1{left:14px;top:14px;width:72px;height:48px;border-radius:50%}
.p2{left:14px;top:88px;width:72px;height:88px;border-radius:6px}
.p3{left:22px;top:186px;width:56px;height:50px;background:linear-gradient(160deg,#f0d46a,#c9a02a);clip-path:polygon(50% 0,100% 80%,0 80%)}

.agents{left:471px;top:741px;font-size:7.4px}
.partner{display:flex;align-items:center;gap:4px;font-weight:700;font-size:10px;color:#222;margin-top:4px}
.partner .sq{width:8px;height:8px;background:#222}
.reg{left:471px;top:805px;font-size:7.2px;line-height:10.5px}

/* business card front */
.card{width:239px;height:155px;overflow:hidden}
.card-front{left:807px;top:130px;background:var(--paper)}
.bc-logo{left:137px;top:38px;font-size:12.5px}
.bc-logo .dot{width:10px;height:10px}
.bc-name{left:15px;top:84px;color:var(--cyan-deep);font-weight:600;font-size:10.5px}
.bc-role{left:15px;top:98px;font-size:6.2px}
.bc-email{left:15px;top:119px;font-size:6.2px}
.bc-email b,.bc-address b{color:var(--cyan-deep)}
.bc-address{left:145px;top:84px;font-size:6.2px;line-height:8px}
.bc-address .web{font-weight:600;color:#222;margin-top:4px}

/* business card backs */
.card-back{left:807px;background:var(--cyan)}
.back-1{top:295px}
.back-2{top:602px}
.card-back .guide-v{background:rgba(255,255,255,.35)}
.back-photo{position:absolute;background:linear-gradient(160deg,#eef0f0,var(--steel) 55%,#7f8486)}
.back-1 .back-photo{left:14px;top:24px;width:120px;height:98px;border-radius:50%}
.back-2 .back-photo{left:22px;top:20px;width:114px;height:120px;border-radius:8px}
.card-back .tagline{color:#fff;left:146px;top:84px;font-size:7.2px;line-height:9px}
</style>
</head>
<body>

<section class="abs letterhead" aria-label="Letterhead">
  <div class="guide-v" style="left:50px"></div>
  <div class="guide-v" style="left:466px"></div>
  <div class="guide-v" style="left:567px"></div>
  <div class="guide-h" style="top:22px"></div>
  <div class="guide-h" style="top:140px"></div>
  <div class="guide-h" style="top:294px"></div>
  <div class="guide-h" style="top:800px"></div>
  <div class="guide-hr" style="top:140px"></div>
  <div class="guide-hr" style="top:294px"></div>
  <div class="guide-hr" style="top:800px"></div>

  <p class="letter date">13 August 2010</p>
  <div class="letter recipient">A N Other<br>1st line of address<br>Town<br>County Postcode</div>
  <div class="letter body">
    <p>Dear Sir/Madam</p>
    <p>Igna faccumsandio dolor sendip enim ex euissed diat, consecte magnibh et ipit vel inciliq uipsums andiam ing erciliqui tio odolor ipsustio od erat lumsan ex eum uatu erosto dui te tie commod ero exeros eum atis amc velenia mcorercidunt er alis dolore consed tat, corpero od molor ing eu feu feumsan eriure feugiat.</p>
    <p>Ut elese modit laorpero od elenit ute mincipisl et, commy nulputpate tie feuis et, vercipsum dignis nummolore magna feum ad magna facidunt loborpe rcillut pationulla facil inciliq uatuerosto dui te tie commod ero exeros eum atis amconsed tat iuscips ustrud endipsustrud modio el duis nibh ercillandre doloreet, quamet, consed magnim dunt vel dolor ing ex et in et adiamet prat, quat ullan henis nonum ad dionsequam, vel ipit iustiss equisi tat. Lestinit adipit augait lortincilis erit nulputpat estisim nulluptatue diam ip er sim etuero dunt do odit numsandre con utat.</p>
    <p>Mod dionse dio consequipisl iustisim dipisse quismodolor sit adigna feuisim del doluptat</p>
  </div>
  <p class="letter signoff">Kind Regards</p>
  <p class="letter signname">Pete Moxham</p>

  <div class="abs brand-mark lh-logo"><span class="dot"></span>BRANDOR</div>

  <div class="abs address">
    Brandor Limited<br>Hollin Offices<br>Hollin Street<br>Ashbrook<br>West Ardenshire<br>United Kingdom
    <div class="gap"></div>
    <b>T</b> 01632 470215<br><b>F</b> 01632 470216<br><b>E</b> sales@brandor.net
    <div class="web">www.brandorparts.co.uk</div>
  </div>

  <p class="abs tagline lh-tagline"><strong>Next day delivery of<br>Cutting tools &amp;<br>Machine tool accessories</strong><br>in the UK &amp; Ireland</p>

  <div class="abs product-grid">
    <div class="product p1" role="img" aria-label="Photo of a face milling cutter"></div>
    <div class="product p2" role="img" aria-label="Photo of three tool holders with end mills"></div>
    <div class="product p3" role="img" aria-label="Photo of a gold carbide insert"></div>
  </div>

  <div class="abs agents">UK agents for
    <div class="partner"><span class="sq"></span>QM-7</div>
    <div class="partner"><span class="sq"></span>VESPANE</div>
  </div>

  <p class="abs reg">Company Registration 5817403<br>Vat No 418 2075 36</p>
</section>

<section class="abs card card-front" aria-label="Business card front">
  <div class="guide-v" style="left:12px"></div>
  <div class="guide-v" style="left:142px"></div>
  <div class="abs brand-mark bc-logo"><span class="dot"></span>BRANDOR</div>
  <p class="abs bc-name">Pete Moxham</p>
  <p class="abs bc-role">General Manager</p>
  <p class="abs bc-email"><b>E</b>&nbsp; pete@brandor.net</p>
  <div class="abs bc-address">
    Brandor Limited<br>Hollin Offices, Hollin Street<br>Ashbrook, West Ardenshire<br>United Kingdom<br>
    <b>T</b> 01632 470215<br><b>F</b> 01632 470216
    <div class="web">www.brandorparts.co.uk</div>
  </div>
</section>

<section class="abs card card-back back-1" aria-label="Business card back">
  <div class="guide-v" style="left:142px"></div>
  <div class="back-photo" role="img" aria-label="Photo of a face milling cutter"></div>
  <p class="abs tagline">Next day delivery of<br><strong>Cutting tools &amp;<br>Machine tool accessories</strong><br>in the UK &amp; Ireland</p>
</section>

<section class="abs card card-back back-2" aria-label="Business card back, alternate">
  <div class="guide-v" style="left:142px"></div>
  <div class="back-photo" role="img" aria-label="Photo of three tool holders with end mills"></div>
  <p class="abs tagline">Next day delivery of<br><strong>Cutting tools &amp;<br>Machine tool accessories</strong><br>in the UK &amp; Ireland</p>
</section>

</body>
</html>
```